Newly constructed college campus housing needs a brochure

We are looking for a brochure that will convey all the cool new ideas that we incorporated into this project . It must appeal to college level ( genY ) people . The name of the project is " Quarry 614 " and has been specifically designed for the needs of todays living needs . It is located in the absolute heart of the Westholm Pacific Institute sub-culture Isla Vista .its a 56 unit building that envelopes very cool features such as a bike repair pod , a study pod , ride share vehicles and a host of other amenities such as on demand endless hot water , Velo silent flush toilets with self closing lids , chalk board walls in every unit , KR top of line appliances that include quiet dishwashers , 25 cubic foot refrigerators , ultra fun and modern kitchens , unique floor and wall tiles from Italia , a large community gathering yard that includes a community BBQ , local artwork AND three large Jacuzzi spas that will accommodate up to 21 people . Quarry 614 has the largest gated parking area in Isla Vista and has over an 100,000 dollar state of the art casino security system and electronic entry gates to assure our tenants privacy and security .
This brochure needs to convey not just the cutting edge building design but also the living features Quarry 614 will offer . Our logo is indicative of the type of student that will reside there " the cool nerd " WPI has many Nobel prize winning professors and most have to do with the engineering programs , these are our target students .

We have decided on the type of printing that we will be using for this project.

The specs are as follows.

4"x9" folded 16"x9" unfolded with .25" bleed.This makes a four panel brochure. Full color. 4/4.

I will be posting site and floor plans later today ( sorry iPad problems ) for site and elevation renderings google Ferrow and Maltby Architects , go to " on the boards " hit Isla Vista student housing . In addition you can view a neighboring project ( different owner ) for more info on area and content example for the area . 
Any other comments questions send them my way , I'm anxious to help in any way possible 

OK group I just garunteed the project as requested and also as requested more photos so I will be opening a snap crate account soon with more photos but feel free to scout photos , for instance young people in a jacuzzi , a young bike mechanic working on a bike , a Rova Dart wheelshare etc. 

 Also as mentioned go to the other projects in town " the Hatch Isla Vista " the " PLUM Isla Vista " both have good appeal to the students and their parents . Keep the comments coming and I will do my best , also Kuddos to the designer that took the initiative to google the area projects and find this one BRAVO !! And if we need 4 pages for the brochure that's fine as well , kids like a lot of pictures 

Hi All,

Please check out the recently added attachments. I have uploaded various images/files that you can include in your brochure.

Attachments include:

1. Project Photos / graphic renderings:

• Courtyard view
• Los Pinos Elevation - view of entrance
• Los Pinos Elevation - view form park
2. Harlow Brandt & Associates logo
3. Quarry 614 logo

4. Floor Plans
• Urban Crib - 1 bed/1 bath (550 sq. ft.)
• Campus Flat - 3 bed / 2 bath (1050 sq. ft.)
• Sky Loft - 2 bed + loft / 2 bath (950 sq. ft.)
5. Quarry 614 Brochure Content
• List of Amenities (unit & site), unit type descriptions, Quarry 614 contact info, etc.
6. Quarry 614 Site Plan

Thanks!

New Sky Loft floor plans have been added.

See attachments: 'sky loft upper floor plan' & 'sky loft floor plan_lower floor'

The specs are as follows.

I have also attached a pdf of brochure-specs. 

See attachment 10 for updated site amenities list.

File name: 'Quarry 614 Brochure content update_01.29.13'

Target Market(s)

Gen Y high caliber engineering students

Industry/Entity Type

Electronic

Requirements
Must have
• Sophisticated , trendy , cool , inviting , fun , conveys friendships . I will download the pictures later and use what you can . We have decided on the type of printing that we will be using for this project.

The specs are as follows.

Should not have
• To much flash

```html
<!DOCTYPE html>
<html lang="en">
<head>
<meta charset="utf-8">
<title>Quarry 614 — Brochure Cover</title>
<link rel="stylesheet" href="https://fonts.googleapis.com/css2?family=Exo+2:wght@300;400;800;900&display=swap">
<style>
  :root {
    --backdrop: #a9a9a9;
    --panel-back: #e7e7e7;
    --panel-front: #ffffff;
    --brand-red: #c0392b;
    --text-grey: #555555;
  }
  * { margin: 0; padding: 0; box-sizing: border-box; }
  html, body { width: 1200px; height: 900px; overflow: hidden; }
  body {
    background: var(--backdrop);
    font-family: "Exo 2", sans-serif;
    position: relative;
  }
  .brochure {
    position: absolute;
    left: 81px; top: 190px;
    width: 1040px; height: 520px;
    display: flex;
  }
  .panel { position: relative; width: 520px; height: 520px; }
  .panel--back { background: var(--panel-back); }
  .panel--front { background: var(--panel-front); }

  .brand-name {
    font-family: "Exo 2", sans-serif;
    font-weight: 800;
    color: var(--brand-red);
    font-size: 30px;
    line-height: 1;
    letter-spacing: 0.5px;
  }
  .brand-address {
    font-family: "Exo 2", sans-serif;
    font-weight: 400;
    color: var(--text-grey);
    font-size: 9px;
    letter-spacing: 0.4px;
    margin-top: 3px;
  }

  .back-identity {
    position: absolute;
    left: 0; width: 520px; top: 228px;
    text-align: center;
  }
  .contact-row {
    position: absolute;
    top: 301px; left: 72px;
    display: flex; gap: 38px;
    list-style: none;
  }
  .contact-item {
    display: flex; align-items: center; gap: 6px;
    font-size: 7.5px; font-weight: 400; color: var(--text-grey);
    letter-spacing: 0.3px;
  }
  .contact-item svg { display: block; }

  .headline {
    position: absolute;
    right: 35px; top: 168px;
    text-align: right;
    font-family: "Exo 2", sans-serif;
    font-weight: 900;
    font-size: 47px;
    line-height: 44px;
    letter-spacing: 0.5px;
    text-transform: uppercase;
  }
  .headline-line {
    display: block;
    color: transparent;
    -webkit-background-clip: text;
    background-clip: text;
  }
  .headline-line--sky { background-image: linear-gradient(90deg, #4f7fc4 0%, #6f96cf 55%, #c9d5e2 100%); }
  .headline-line--street { background-image: linear-gradient(90deg, #8a2b22 0%, #b84032 25%, #5f7d3c 55%, #8a6d4c 80%, #3b3b3b 100%); }
  .headline-line--plaza { background-image: linear-gradient(90deg, #a3271e 0%, #6e7a3a 40%, #c9a93a 65%, #5a4b3a 100%); }
  .headline-line--walk { background-image: linear-gradient(90deg, #6c6a64 0%, #8d8472 50%, #b9ad8f 100%); }

  .front-identity {
    position: absolute;
    right: 35px; top: 352px;
    text-align: right;
  }
</style>
</head>
<body>
  <main class="brochure">
    <section class="panel panel--back">
      <div class="back-identity">
        <div class="brand-name">QUARRY 614</div>
        <div class="brand-address">614 CAMINO LOS PINOS ISLA VISTA, CA&nbsp; 93117</div>
      </div>
      <ul class="contact-row">
        <li class="contact-item">
          <svg width="16" height="12" viewBox="0 0 16 12" aria-hidden="true">
            <rect x="1" y="1" width="14" height="8" fill="none" stroke="#c0392b" stroke-width="1.5"/>
            <rect x="6" y="9" width="4" height="2" fill="#c0392b"/>
            <rect x="4" y="11" width="8" height="1" fill="#c0392b"/>
          </svg>
          WWW.HARLOWBRANDTIV.COM
        </li>
        <li class="contact-item">
          <svg width="17" height="12" viewBox="0 0 17 12" aria-hidden="true">
            <rect x="0" y="0" width="17" height="12" fill="#c0392b"/>
            <path d="M0 0 L8.5 7 L17 0" fill="none" stroke="#ffffff" stroke-width="1.2"/>
          </svg>
          LEASING@HARLOWBRANDTIV.COM
        </li>
        <li class="contact-item">
          <svg width="8" height="13" viewBox="0 0 8 13" aria-hidden="true">
            <rect x="0.75" y="0.75" width="6.5" height="11.5" rx="1" fill="none" stroke="#c0392b" stroke-width="1.5"/>
            <rect x="3" y="9.5" width="2" height="1.2" fill="#c0392b"/>
          </svg>
          (805) 555-0142
        </li>
      </ul>
    </section>

    <section class="panel panel--front">
      <h1 class="headline" aria-label="Advanced living for an advanced world">
        <span class="headline-line headline-line--sky">Advanced</span>
        <span class="headline-line headline-line--street">Living for an</span>
        <span class="headline-line headline-line--plaza">Advanced</span>
        <span class="headline-line headline-line--walk">World</span>
      </h1>
      <div class="front-identity">
        <div class="brand-name">QUARRY 614</div>
        <div class="brand-address">614 CAMINO LOS PINOS ISLA VISTA, CA&nbsp; 93117</div>
      </div>
    </section>
  </main>
</body>
</html>
```